Reed Lantern Cannabis Cartridge box

Box with both inside and outside box. A disposable cannabis vape cart is the contents of the package. initial thoughts were black exterior box with color highlight. (example of 7 mint attached). There are four colors currently being used for the actual product. Black, White, Green and Blue. product will sit in retail display box. It should both "pop" and still emote quality and class.

Target Market(s)

Professional, discreet cannabis consumer. Experienced and knowledgeable

Industry/Entity Type

Cannabis

Font styles to use
Serif

Colors

Designer to choose colors to be used in the design.

Requirements
Must have
• use logo and logo colors
Nice to have
• elegant look. metalic foil printing, embossing available

```html
<!DOCTYPE html>
<html lang="en">
<head>
<meta charset="utf-8">
<title>Reed Lantern Cannabis Cartridge Box – Dieline</title>
<link rel="stylesheet" href="https://fonts.googleapis.com/css2?family=Poppins:wght@400;500;600;700&family=Oswald:wght@400;500&display=swap">
<style>
  :root{
    --paper:#ffffff;
    --board:#262828;
    --cut:#d8262e;
    --white:#ffffff;
    --teal:#00a886;
    --blue:#1a8fd0;
    --alert:#e5232b;
  }
  html,body{margin:0;padding:0;width:1200px;height:903px;overflow:hidden;background:var(--paper);}
  .dieline-sheet{display:block;width:1200px;height:903px;}
  .board{fill:var(--board);stroke:var(--cut);stroke-width:1.5;}
  .fold{fill:none;stroke:var(--cut);stroke-width:1;}
  .hole{fill:none;stroke:var(--cut);stroke-width:1.2;}
  .accent-band{fill:var(--teal);}
  .body-copy{font-family:'Poppins',sans-serif;fill:var(--white);font-size:19px;}
  .section-title{font-family:'Poppins',sans-serif;fill:var(--teal);font-size:21px;font-weight:500;}
  .warning-label{font-family:'Poppins',sans-serif;fill:var(--alert);font-size:15px;font-weight:500;}
  .warning-copy{font-family:'Poppins',sans-serif;fill:var(--white);font-size:15.5px;}
  .warning-frame{fill:none;stroke:var(--white);stroke-width:1.5;}
  .brand-name{font-family:'Poppins',sans-serif;fill:var(--blue);font-size:29px;font-weight:700;}
  .brand-side{font-family:'Poppins',sans-serif;fill:var(--white);font-size:46px;font-weight:700;}
  .product-kicker{font-family:'Oswald',sans-serif;fill:var(--white);font-size:28px;letter-spacing:15px;font-weight:500;}
  .product-line{font-family:'Poppins',sans-serif;fill:var(--teal);font-size:29px;font-weight:700;}
  .product-type{font-family:'Poppins',sans-serif;fill:var(--white);font-size:29px;font-weight:700;}
  .spec{font-family:'Poppins',sans-serif;fill:var(--white);font-size:18px;}
  .caution{font-family:'Oswald',sans-serif;fill:var(--white);font-size:19px;}
  .side-copy{font-family:'Poppins',sans-serif;fill:var(--white);font-size:17.5px;}
  .side-copy .strong{font-weight:700;}
</style>
</head>
<body>
<svg class="dieline-sheet" viewBox="0 0 2200 1656" xmlns="http://www.w3.org/2000/svg">

  <!-- Outer carton -->
  <g class="outer-carton">
    <!-- top flaps -->
    <rect class="board" x="186" y="267" width="338" height="180" rx="22"/>
    <rect class="board" x="522" y="292" width="160" height="150" rx="14"/>
    <rect class="board" x="678" y="244" width="354" height="200" rx="22"/>
    <rect class="board" x="1030" y="292" width="164" height="150" rx="20"/>
    <!-- bottom flaps -->
    <rect class="board" x="180" y="1340" width="338" height="138" rx="22"/>
    <rect class="board" x="514" y="1340" width="180" height="138" rx="14"/>
    <rect class="board" x="688" y="1340" width="330" height="138" rx="14"/>
    <rect class="board" x="1014" y="1340" width="186" height="138" rx="22"/>
    <!-- body -->
    <rect class="board" x="85" y="425" width="1120" height="935" rx="22"/>
    <rect class="accent-band" x="90" y="1315" width="1114" height="36"/>

    <g class="fold">
      <line x1="200" y1="436" x2="1183" y2="436"/>
      <line x1="200" y1="1350" x2="1183" y2="1350"/>
      <line x1="200" y1="436" x2="200" y2="1350"/>
      <line x1="515" y1="436" x2="515" y2="1350"/>
      <line x1="692" y1="436" x2="692" y2="1350"/>
      <line x1="1015" y1="436" x2="1015" y2="1350"/>
      <line x1="1183" y1="436" x2="1183" y2="1350"/>
      <line x1="105" y1="448" x2="105" y2="1340"/>
      <polyline points="208,415 208,289 502,289 502,405 515,430 530,405 530,314 677,314 677,405 692,430 698,405 698,266 1010,266 1010,405 1015,430 1030,405 1030,314 1170,314 1170,405 1183,430"/>
      <polyline points="202,1380 202,1457 506,1457 506,1370 515,1358 527,1370 527,1457 680,1457 680,1370 692,1358 702,1370 702,1457 1006,1457 1006,1370 1015,1358 1027,1370 1027,1457 1177,1457 1177,1370 1183,1358"/>
    </g>
    <circle class="hole" cx="604" cy="1167" r="42"/>
    <path class="hole" d="M538,1350 A66,66 0 0 1 669,1350"/>
    <path class="hole" d="M1033,1350 A66,66 0 0 1 1164,1350"/>

    <!-- back panel -->
    <g class="panel-back">
      <text class="section-title" x="356" y="496" text-anchor="middle">Our Story</text>
      <text class="body-copy" text-anchor="middle">
        <tspan x="360" y="540">Lorem ipsum dolor sit amet,</tspan>
        <tspan x="360" y="560">consectetuer adipiscing elit,</tspan>
        <tspan x="360" y="581">sed diam nonummy nibh</tspan>
        <tspan x="360" y="601">euismod tincidunt ut laoreet</tspan>
        <tspan x="360" y="622">dolore magna aliquam erat</tspan>
        <tspan x="360" y="642">volutpat.</tspan>
        <tspan x="360" y="683">t wisi enim ad minim veniam,</tspan>
        <tspan x="360" y="703">quis nostrud exerci tation</tspan>
        <tspan x="360" y="724">ullamcorper suscipit lobortis</tspan>
        <tspan x="360" y="744">nisl ut aliquip ex ea commo-</tspan>
        <tspan x="360" y="765">do consequat. Duis autem vel</tspan>
        <tspan x="360" y="785">eum iriure dolor in hendrerit</tspan>
        <tspan x="360" y="806">in vulputate velit esse</tspan>
        <tspan x="360" y="826">molestie consequat, vel illum</tspan>
        <tspan x="360" y="847">dolore eu feugiat</tspan>
      </text>
      <rect class="warning-frame" x="222" y="902" width="276" height="122"/>
      <text class="warning-label" x="358" y="924" text-anchor="middle">WARNING:</text>
      <text class="warning-copy" text-anchor="middle">
        <tspan x="358" y="945">Lorem ipsum dolor sit amet,</tspan>
        <tspan x="358" y="966">consectetuer adipiscing elit, sed</tspan>
        <tspan x="358" y="986">diam nonummy nibh euismod</tspan>
        <tspan x="358" y="1007">tincidunt ut</tspan>
      </text>
    </g>

    <!-- left side panel -->
    <text class="side-copy" transform="translate(639,482) rotate(90)">
      <tspan x="0" y="0"><tspan class="strong">DO NOT EAT</tspan> For use only by adults 21 and</tspan>
      <tspan x="0" y="21">older. Keep out of reach of children.</tspan>
      <tspan x="0" y="42">Do not drive a motor vehicle while under</tspan>
      <tspan x="0" y="63">the influence of marijuana</tspan>
    </text>

    <!-- front panel -->
    <g class="panel-front">
      <circle cx="853" cy="540" r="9" fill="var(--teal)"/>
      <text class="brand-name" x="853" y="610" text-anchor="middle">Reed Lantern</text>
      <text class="product-kicker" x="855" y="748" text-anchor="middle">DISPOSABLE</text>
      <line x1="729" y1="762" x2="977" y2="762" stroke="var(--teal)" stroke-width="2"/>
      <text class="product-line" x="850" y="798" text-anchor="middle">CANNABIS VAPE</text>
      <text class="product-type" x="850" y="829" text-anchor="middle">CARTRIDGE</text>
      <text class="spec" x="798" y="896" text-anchor="middle">1 mL/250 mg</text>
      <line x1="872" y1="873" x2="872" y2="905" stroke="var(--teal)" stroke-width="2"/>
      <text class="spec" x="933" y="896" text-anchor="middle">99% CBD</text>
      <rect x="798" y="1104" width="100" height="70" rx="6" fill="var(--alert)" role="img" aria-label="Cannabis warning symbol"/>
      <text class="caution" x="854" y="1205" text-anchor="middle">CONTAINING MARIJUANA</text>
      <text class="caution" x="854" y="1236" text-anchor="middle">KEEP OUT OF THE REACH OF CHILDREN</text>
    </g>

    <!-- right side panel -->
    <text class="side-copy" transform="translate(1076,1245) rotate(-90)">
      <tspan x="0" y="0">Suggested serving size is one 5 second draw.</tspan>
      <tspan x="0" y="21">Each cartridge provides about 150 servings with a 5</tspan>
      <tspan x="0" y="42">second draw.</tspan>
    </text>
  </g>

  <!-- Inner tray -->
  <g class="inner-tray">
    <rect class="board" x="1525" y="124" width="316" height="290" rx="22"/>
    <rect class="board" x="1525" y="1285" width="316" height="290" rx="22"/>
    <rect class="board" x="1383" y="294" width="144" height="120" rx="20"/>
    <rect class="board" x="1840" y="294" width="144" height="120" rx="20"/>
    <rect class="board" x="1383" y="1285" width="144" height="120" rx="20"/>
    <rect class="board" x="1840" y="1285" width="144" height="120" rx="20"/>
    <rect class="board" x="1262" y="390" width="844" height="918" rx="22"/>

    <g class="fold">
      <rect x="1397" y="402" width="573" height="894"/>
      <line x1="1540" y1="402" x2="1540" y2="1296"/>
      <line x1="1828" y1="402" x2="1828" y2="1296"/>
      <rect x="1283" y="410" width="800" height="877"/>
      <line x1="1385" y1="410" x2="1385" y2="1287"/>
      <line x1="1983" y1="410" x2="1983" y2="1287"/>
      <polyline points="1545,390 1545,145 1819,145 1819,390"/>
      <line x1="1545" y1="246" x2="1819" y2="246"/>
      <line x1="1545" y1="259" x2="1819" y2="259"/>
      <polyline points="1545,1308 1545,1552 1819,1552 1819,1308"/>
      <line x1="1545" y1="1440" x2="1819" y2="1440"/>
      <line x1="1545" y1="1452" x2="1819" y2="1452"/>
      <polyline points="1383,380 1408,315 1506,315 1540,395"/>
      <polyline points="1828,395 1860,315 1960,315 1983,380"/>
      <polyline points="1383,1318 1408,1383 1506,1383 1540,1303"/>
      <polyline points="1828,1303 1860,1383 1960,1383 1983,1318"/>
    </g>
    <circle class="hole" cx="1898" cy="1120" r="42"/>

    <text class="brand-side" transform="translate(1488,838) rotate(-90)" text-anchor="middle">Reed Lantern</text>
    <text class="brand-side" transform="translate(1880,838) rotate(90)" text-anchor="middle">Reed Lantern</text>
  </g>
</svg>
</body>
</html>
```